Broschüre für Softwareentwickler
Zielgruppe
Softwareentwicklung für die Immobilienwirtschaft, speziell Bauträger, Projektentwickler und Generalunternehmer. ROLDA ist eine von uns - Harbeck Software und Beratung AG - entwickelte Branchensoftware für die kaufmännische Abwicklung der Prozesse in der Immobilienwirtschaft.
Aufgabenstellung
Wir wollen unseren aktuellen Flyer/Broschüre für unsere Software ROLDA überarbeiten lassen. Es soll weiterhin/quer in der Mitte gefaltet sein - 4-seiter - sein. Das Firmenlogo wurde zwischenzeitlich geändert und finden Sie im Anhang. Das Logo für die Software ROLDA soll so erhalten bleiben (finden Sie ebenfalls im Anhang).
Beide Logos sollen farbunabhängig sein und auch als Outline sowie invertiert abgebildet werden können. Das Logo-Blau vom Produktlogo ROLDA muss nicht erhalten bleiben, wir möchten eher weg von Blau.
Das aktuell im Flyer enthaltenen Bilder sollen verändert/nicht mehr genutzt werden. Das Layout der Broschüre soll angepasst werden. Wir wollen hier neue Bilder/andere Bilder verwenden. Mehr in Anlehnung an die Homepage-Bilder.
Der Textumfang wird gleich bleiben, wird aber noch angepasst - kommt noch.
Die Aufteilung und die Positionen der Texte/Bilder dürfen gerne verändert werden. Wir freuen uns über kreative, ganz neue Designzusammenstellungen.

```html
<!DOCTYPE html>
<html lang="de">
<head>
<meta charset="utf-8">
<title>ROLDA – Broschüre</title>
<link href="https://fonts.googleapis.com/css2?family=Open+Sans:wght@300;400;600;700;800&display=swap" rel="stylesheet">
<style>
  :root{
    --brand-blue:#1b4a9c;
    --brand-blue-dark:#143d88;
    --lavender:#8a90c2;
    --text-grey:#555a62;
    --stage:#e6e7ea;
    --paper-top:#ffffff;
    --paper-bottom:#e4e5e8;
  }
  *{box-sizing:border-box;margin:0;padding:0}
  html,body{width:1200px;height:1006px;overflow:hidden}
  body{background:var(--stage);font-family:"Open Sans",sans-serif;position:relative}
  .spread{position:absolute;left:60px;top:121px;width:1080px;height:764px;display:flex;box-shadow:0 12px 30px rgba(0,0,0,.18)}
  .page{position:relative;width:540px;height:764px;overflow:hidden;
    background:linear-gradient(160deg,var(--paper-top) 0%,#f3f3f5 50%,var(--paper-bottom) 100%)}
  .page-shapes{position:absolute;inset:0}
  /* back cover */
  .about-text{position:absolute;left:30px;top:300px;width:480px;font-size:11.4px;line-height:1.5;color:var(--text-grey);text-align:justify}
  .about-text .closing{margin-top:16px;text-align:left}
  .product-badge{position:absolute;left:385px;top:525px;width:135px;height:140px;border-radius:18px;background:var(--brand-blue);
    display:flex;align-items:center;justify-content:center}
  .product-badge span{color:#fff;font-weight:700;font-size:30px;letter-spacing:1px}
  .contact{position:absolute;left:30px;top:585px;font-size:11px;line-height:1.4;color:var(--text-grey);font-style:normal}
  .contact .company{color:var(--brand-blue);font-weight:700}
  .contact ul{list-style:none;margin-top:4px}
  .contact li{display:flex;align-items:center;gap:8px}
  .contact li svg{width:12px;height:12px;flex:none}
  .contact .tagline{margin-top:5px;font-size:9.5px;line-height:1.35}
  /* front cover */
  .cover-product{position:absolute;right:40px;top:40px;color:#fff;font-weight:700;font-size:19px;letter-spacing:1px}
  .headline{position:absolute;left:80px;top:440px;width:450px;color:var(--brand-blue);font-weight:800;font-size:30px;line-height:1.2}
  .subline{position:absolute;left:84px;top:522px;color:var(--lavender);font-weight:600;font-size:15px;letter-spacing:.3px}
  .company-name{position:absolute;left:84px;top:550px;color:#222;font-weight:300;font-size:28px}
</style>
</head>
<body>
<main class="spread">

  <section class="page back-cover">
    <svg class="page-shapes" viewBox="0 0 540 764">
      <defs>
        <linearGradient id="contactPhoto" x1="0" y1="0" x2="1" y2="1">
          <stop offset="0" stop-color="#6e6a86"/>
          <stop offset=".45" stop-color="#c9a79c"/>
          <stop offset="1" stop-color="#ece8e0"/>
        </linearGradient>
      </defs>
      <path role="img" aria-label="Foto: Hände halten ein Smartphone mit Kontaktsymbolen" fill="url(#contactPhoto)"
            d="M0,40 H400 L222,238 Q212,250 196,250 H0 Z"/>
      <path class="accent-band" fill="var(--brand-blue)"
            d="M420,0 H540 V30 L330,240 Q320,252 304,252 H245 Z"/>
    </svg>

    <div class="about-text">
      <p>Harbeck Software und Beratung AG hat sich ein klar definiertes Ziel gesetzt: die kontinuierliche Perfektionierung der Leistungen unserer Mitarbeiter und der von uns angebotenen Technologien. All unsere Kompetenz, jahrelange Branchenerfahrung und Energie fließen in die Entwicklung effizienter Softwarelösungen und umfassender Unternehmensberatung. Das gemeinsame Anliegen unseres Teams und unserer Kunden ist wirtschaftlicher Erfolg. Die Basis eines jeden Erfolges sind fachspezifisches Wissen, leistungsstarke Verfahren und der Wille, beides ständig zu erneuern und zu erweitern. Denn Stillstand heißt Rückschritt. Dieses erklärte Ziel macht uns zu Partnern und wenn diese Partnerschaft funktionieren soll, sind zwei Faktoren unentbehrlich: Offenheit und Vertrauen. Nur so erreichen wir ein Optimum von Kreativität und Konstruktivität. Was daraus folgt, sind kunden- und marktorientierte Lösungen und die absolute Zufriedenheit eines jeden Einzelnen. Das ist der Anspruch unserer Arbeit.</p>
      <p class="closing">Gestern, heute und in Zukunft.</p>
    </div>

    <div class="product-badge"><span>ROLDA</span></div>

    <address class="contact">
      <div class="company">Harbeck Software und Beratung AG</div>
      <div>Lindenhof-Str. 12<br>74391 Erlenbach<br>Germany</div>
      <ul>
        <li><svg viewBox="0 0 14 14"><rect width="14" height="14" rx="3" fill="var(--brand-blue)"/><path d="M4 3.5l1.6-.3.8 2-1 .8a6 6 0 0 0 2.6 2.6l.8-1 2 .8-.3 1.6c-3.6.2-6.7-2.9-6.5-6.5z" fill="#fff"/></svg>+49 (0) 7143 5820 100</li>
        <li><svg viewBox="0 0 14 14"><rect width="14" height="14" rx="3" fill="var(--brand-blue)"/><rect x="3.5" y="3" width="7" height="3" fill="#fff"/><rect x="2.5" y="6" width="9" height="4.5" rx="1" fill="#fff"/></svg>+49 (0) 7143 5820 155</li>
        <li><svg viewBox="0 0 14 14"><rect width="14" height="14" rx="3" fill="var(--brand-blue)"/><rect x="3" y="4" width="8" height="6" fill="#fff"/><path d="M3 4l4 3.3L11 4" stroke="var(--brand-blue)" fill="none"/></svg>info@rolda-software.de</li>
        <li><svg viewBox="0 0 14 14"><rect width="14" height="14" rx="3" fill="var(--brand-blue)"/><circle cx="7" cy="7" r="3.8" stroke="#fff" fill="none"/><path d="M3.2 7h7.6M7 3.2v7.6" stroke="#fff"/></svg>www.rolda-software.de</li>
      </ul>
      <p class="tagline">Sichern Sie sich unsere Beratungskompetenz –<br>wir helfen Ihnen weiter!</p>
    </address>
  </section>

  <section class="page front-cover">
    <svg class="page-shapes" viewBox="0 0 540 764">
      <defs>
        <linearGradient id="skylinePhoto" x1="0" y1="0" x2="0" y2="1">
          <stop offset="0" stop-color="#e8dccb"/>
          <stop offset=".35" stop-color="#b79a82"/>
          <stop offset="1" stop-color="#5f5650"/>
        </linearGradient>
      </defs>
      <path class="accent-band" fill="var(--brand-blue)"
            d="M275,0 H540 V150 L395,305 Q380,320 360,320 H320 L445,175 Q465,150 440,125 L335,20 Z"/>
      <path role="img" aria-label="Foto: Skyline einer Großstadt im Abendlicht" fill="url(#skylinePhoto)"
            d="M0,0 H370 Q395,0 412,17 L445,50 Q465,72 448,95 L255,375 Q235,400 210,385 L40,270 Q0,245 0,200 Z"/>
      <path class="stripe-light" fill="var(--lavender)" d="M370,764 L495,665 Q505,657 520,657 H540 V668 L425,764 Z"/>
      <path class="stripe-dark" fill="var(--brand-blue)" d="M418,764 L508,690 Q520,680 535,686 L540,688 V764 Z"/>
    </svg>

    <div class="cover-product">ROLDA</div>
    <h1 class="headline">Die ganzheitliche Lösung<br>für Ihr Unternehmen</h1>
    <p class="subline">Die Bauträger-Software</p>
    <p class="company-name">harbeck</p>
  </section>

</main>
</body>
</html>
```